Tavenored Crest

Need very crisp business cards for Tavenor Crest per the logo attached. The vision of Tavenor Crest is 'Steer every Venture to Tavenor'. I am going into Freelance | Consulting | Contracting and need this communicated on the card. I need the card to provide a clear message of professionalism and what the vision emulates. Will need an area for my website, LinkedIn, Twitter, as fell as the obvious Name, Address, phone, email... on the back, I would like the Vision but receptive to your design ideas.

```html
<!DOCTYPE html>
<html lang="en">
<head>
<meta charset="utf-8">
<title>Tavenored Crest – Business Card</title>
<link rel="stylesheet" href="https://fonts.googleapis.com/css2?family=Montserrat:wght@400;500;600;700&display=swap">
<style>
  :root {
    --stage: #3a3c40;
    --card-white: #ffffff;
    --card-black: #050505;
    --navy: #0d2a6b;
    --steel-blue: #4a6a9c;
    --charcoal: #2b2b2d;
    --ink: #2a2a2a;
    --sheen: #7a7a7c;
    --sheen-mid: #2c2c2e;
    --tagline-light: #d8d8d8;
  }
  * { box-sizing: border-box; margin: 0; padding: 0; }
  html, body { width: 1200px; height: 900px; overflow: hidden; }
  body {
    background: var(--stage);
    font-family: "Montserrat", sans-serif;
    position: relative;
  }
  .card {
    position: absolute;
    width: 640px;
    height: 366px;
    border-radius: 26px;
    overflow: hidden;
  }

  /* Brand lockup shared */
  .brand {
    position: absolute;
    display: flex;
    align-items: center;
    gap: 12px;
  }
  .brand-mark { width: 34px; height: 34px; flex: none; }
  .brand-text { display: flex; flex-direction: column; }
  .brand-name {
    font-size: 30px;
    font-weight: 500;
    line-height: 1;
    white-space: nowrap;
  }
  .brand-tagline {
    margin-top: 5px;
    font-size: 7.5px;
    font-weight: 500;
    letter-spacing: 2.6px;
    text-transform: uppercase;
    text-align: right;
    white-space: nowrap;
  }

  /* Back side */
  .card-back {
    left: 60px;
    top: 60px;
    background: var(--card-black);
  }
  .back-texture {
    position: absolute;
    inset: 0;
    background:
      linear-gradient(115deg, transparent 18%, rgba(122,122,124,0.55) 42%, rgba(122,122,124,0.35) 55%, transparent 78%),
      radial-gradient(ellipse at 50% 35%, var(--sheen) 0%, var(--sheen-mid) 50%, var(--card-black) 85%);
    opacity: 0.8;
  }
  .back-plate {
    position: absolute;
    left: 150px;
    top: 206px;
    width: 360px;
    height: 64px;
    background: var(--card-black);
  }
  .card-back .brand { left: 166px; top: 216px; }
  .card-back .brand-mark { background: #ffffff; }
  .card-back .brand-name { color: #ffffff; }
  .card-back .brand-tagline { color: var(--tagline-light); }

  /* Front side */
  .card-front {
    left: 500px;
    top: 474px;
    background: var(--card-white);
  }
  .card-front .brand { left: 300px; top: 58px; }
  .card-front .brand-mark { background: var(--navy); }
  .card-front .brand-name { color: var(--navy); }
  .card-front .brand-tagline { color: var(--navy); }

  .divider {
    position: absolute;
    left: 150px;
    right: 0;
    top: 176px;
    height: 2px;
    background: var(--navy);
  }
  .holder-name {
    position: absolute;
    left: 160px;
    top: 134px;
    font-size: 32px;
    font-weight: 600;
    line-height: 1;
    color: var(--ink);
    letter-spacing: 0.5px;
  }
  .holder-name .first { color: var(--navy); }

  .social {
    position: absolute;
    left: 210px;
    top: 206px;
    display: flex;
    gap: 22px;
  }
  .social-tile {
    width: 44px;
    height: 44px;
    border-radius: 9px;
    background: var(--steel-blue);
  }

  .contact-list {
    position: absolute;
    left: 405px;
    top: 190px;
    list-style: none;
  }
  .contact-list li {
    display: flex;
    align-items: center;
    gap: 12px;
    font-size: 14px;
    font-weight: 600;
    color: var(--ink);
    height: 23px;
  }
  .contact-list svg { width: 14px; height: 14px; fill: var(--navy); flex: none; }

  .front-footer {
    position: absolute;
    left: 0;
    bottom: 0;
    width: 640px;
    height: 60px;
  }
</style>
</head>
<body>
  <section class="card card-back" aria-label="Business card back">
    <div class="back-texture" role="img" aria-label="Repeating brand monogram pattern in silver on black"></div>
    <div class="back-plate"></div>
    <div class="brand">
      <span class="brand-mark"></span>
      <span class="brand-text">
        <span class="brand-name">Tavenored Crest</span>
        <span class="brand-tagline">Steer every Venture to Tavenor</span>
      </span>
    </div>
  </section>

  <section class="card card-front" aria-label="Business card front">
    <div class="brand">
      <span class="brand-mark"></span>
      <span class="brand-text">
        <span class="brand-name">Tavenored Crest</span>
        <span class="brand-tagline">Steer every Venture to Tavenor</span>
      </span>
    </div>

    <div class="holder-name"><span class="first">FULL</span> NAME</div>
    <div class="divider"></div>

    <div class="social" aria-label="Social profiles">
      <span class="social-tile"></span>
      <span class="social-tile"></span>
    </div>

    <ul class="contact-list">
      <li><svg viewBox="0 0 16 16"><path d="M3 1l3 0 1 4-2 1c1 2 3 4 5 5l1-2 4 1 0 3c0 1-1 2-2 2C7 15 1 9 1 3c0-1 1-2 2-2z"/></svg>Phone Number</li>
      <li><svg viewBox="0 0 16 16"><path d="M1 3h14v10H1z"/><path d="M1 3l7 6 7-6" fill="none" stroke="#fff" stroke-width="1.2"/></svg>E-mail</li>
      <li><svg viewBox="0 0 16 16"><path d="M8 1a5 5 0 0 1 5 5c0 4-5 9-5 9S3 10 3 6a5 5 0 0 1 5-5zm0 3a2 2 0 1 0 0 4 2 2 0 0 0 0-4z"/></svg>Adresse</li>
      <li><svg viewBox="0 0 16 16"><circle cx="8" cy="8" r="7"/><path d="M1 8h14M8 1c-3 4-3 10 0 14M8 1c3 4 3 10 0 14" fill="none" stroke="#fff" stroke-width="1"/></svg>Website</li>
    </ul>

    <svg class="front-footer" viewBox="0 0 640 60" preserveAspectRatio="none" aria-hidden="true">
      <polygon points="0,42 640,42 640,60 0,60" fill="var(--charcoal)"/>
      <polygon points="300,42 350,20 640,20 640,42" fill="var(--steel-blue)"/>
    </svg>
  </section>
</body>
</html>
```